New Web Site - Professional Cleaning Company

I want to create a new attractive website that acts as an advertisement to visitors to entice them to reach out for more information.
We are a commercial/business janitorial service - with a new logo, would like the font to be complimentary to the font of logo, as well as the color scheme.
Target Market(s)
Commercial buildings, schools & medical buildings
Industry/Entity Type
Janitorial
Coding
Coded - Design and coding required
Number of Pages Required
4 page
Requirements
Must have
- Professionalism, sharp imagery

```html
<!DOCTYPE html>
<html lang="en">
<head>
<meta charset="utf-8">
<title>Brightwell Facility Services</title>
<link rel="stylesheet" href="https://fonts.googleapis.com/css2?family=Michroma&family=Roboto:wght@400;500;700&display=swap">
<style>
:root{
  --navy:#1b2a6b;
  --navy-dark:#131e4f;
  --blue:#1f86cf;
  --sky:#2d9bd9;
  --green:#3bb54a;
  --grey:#eef0f4;
  --text:#555b66;
  --white:#fff;
}
*{box-sizing:border-box;margin:0;padding:0}
html,body{width:1200px;height:4286px;overflow:hidden}
body{position:relative;font-family:'Roboto',sans-serif;color:var(--text);background:var(--white)}
.abs{position:absolute}
.display{font-family:'Michroma',sans-serif;color:#111;font-weight:400}
.btn{position:absolute;display:flex;align-items:center;justify-content:center;gap:10px;border-radius:24px;color:#fff;font-weight:700;font-size:13px;letter-spacing:.3px}
.btn .arrow{width:14px;height:14px;border-radius:50%;background:#fff;display:inline-flex;align-items:center;justify-content:center}
.btn .arrow::after{content:"";border-left:5px solid var(--navy);border-top:4px solid transparent;border-bottom:4px solid transparent;margin-left:2px}

/* header */
.topbar{top:0;left:0;width:1200px;height:95px;background:#fff}
.navbar{top:95px;left:0;width:1200px;height:42px;background:var(--navy)}
.nav{position:absolute;right:112px;top:0;height:42px;display:flex;align-items:center;gap:36px;list-style:none}
.nav li{color:#fff;font-size:13px;font-weight:700}
.brand{top:8px;left:112px;width:140px;height:140px;border-radius:50%;background:#fff;border:4px solid var(--navy);display:flex;align-items:center;justify-content:center;flex-direction:column;z-index:3;box-shadow:0 2px 8px rgba(0,0,0,.15)}
.brand span{font-family:'Roboto',sans-serif;font-weight:700;color:var(--navy);font-size:15px;text-align:center;line-height:1.2}
.socials{display:flex;gap:8px}
.socials i{display:block;width:30px;height:30px;border-radius:50%;background:var(--blue)}
.hotline{top:26px;left:758px;display:flex;align-items:center;gap:12px}
.hotline small{display:block;font-size:13px;font-weight:700;color:#111}
.hotline b{display:block;font-size:21px;color:var(--blue)}
.mascot{top:20px;left:1005px;width:84px;height:78px;border-radius:40px 40px 10px 10px;background:var(--green)}

/* hero */
.hero{top:137px;left:0;width:1200px;height:650px;background:linear-gradient(180deg,#e9ebee 0%,#d7dadf 55%,#eef0f2 100%)}
.hero h1{position:absolute;left:110px;top:110px;font-size:36px;line-height:50px}
.hero h1 em{font-style:normal;color:var(--blue)}
.hero p{position:absolute;left:110px;top:275px;width:480px;font-size:15px;line-height:26px;color:#555}
.slide-arrow{width:32px;height:32px;border-radius:50%;background:#fff;box-shadow:0 2px 6px rgba(0,0,0,.2);display:flex;align-items:center;justify-content:center}
.slide-arrow::after{content:"";width:9px;height:9px;border-left:2px solid #222;border-bottom:2px solid #222}
.hero-photo{left:664px;top:70px;width:426px;height:426px;border-radius:50%;border:20px solid var(--blue);background:linear-gradient(135deg,#c9ced6,#8d96a3 60%,#5d6673)}

/* target */
.target{top:782px;left:0;width:1200px;height:535px;background:var(--grey)}
.section-title{position:absolute;left:0;width:1200px;text-align:center;font-size:28px}
.card{position:absolute;top:150px;width:310px;height:308px;border-radius:8px;overflow:hidden}
.card .label{position:absolute;bottom:46px;left:0;width:100%;text-align:center;color:#fff;font-family:'Michroma',sans-serif;font-size:14px}
.card.photo-a{background:linear-gradient(180deg,#3c5b82,#1d2b3f 70%,#2b2b2b)}
.card.photo-b{background:linear-gradient(180deg,#9fb9d9,#c4c9cf 55%,#8a8f94)}
.card.feature{background:var(--navy);border:4px solid var(--green);box-shadow:0 10px 24px rgba(27,42,107,.3);text-align:center;color:#fff}
.feature .badge{width:72px;height:72px;border-radius:50%;background:#fff;border:5px solid var(--blue);margin:44px auto 22px;display:flex;align-items:center;justify-content:center}
.feature h3{font-family:'Michroma',sans-serif;font-size:15px;font-weight:400;margin-bottom:12px}
.feature p{font-size:13px;line-height:22px;width:250px;margin:0 auto}
.feature .go{width:16px;height:16px;border-radius:50%;background:#fff;margin:14px auto 0;display:flex;align-items:center;justify-content:center}
.feature .go::after{content:"";border-left:5px solid var(--navy);border-top:4px solid transparent;border-bottom:4px solid transparent;margin-left:2px}

/* about */
.about-photo{left:128px;top:1414px;width:426px;height:426px;border-radius:50%;border:22px solid var(--blue);background:linear-gradient(160deg,#cfd7d2,#7e8f7f 55%,#3f5a49)}
.sparkle{color:var(--blue);font-size:30px;font-weight:300}
.about h2{position:absolute;left:622px;top:1445px;font-size:27px}
.about p{position:absolute;left:622px;top:1518px;width:465px;font-size:14px;line-height:25.8px;text-align:justify;color:#6a6f78}

/* why */
.why{top:1930px;left:0;width:1200px;height:800px}
.why-head{position:absolute;left:0;width:1200px;text-align:center;color:#fff}
.why-item{position:absolute;color:#fff;font-weight:700;font-size:20px;line-height:26px}
.why-item.left{text-align:right}
.why-icon{position:absolute;width:66px;height:66px;border-radius:50%;background:#fff;box-shadow:0 4px 10px rgba(0,0,0,.15);display:flex;align-items:center;justify-content:center}

/* testimonials */
.quote{position:absolute;top:2920px;width:310px;height:118px;background:#fff;border-radius:8px;box-shadow:0 4px 18px rgba(0,0,0,.12);padding:22px 24px;font-style:italic;font-size:13px;line-height:20px;color:#666}
.quote b{position:absolute;right:24px;bottom:14px;font-style:normal;font-size:42px;color:var(--blue);line-height:30px;font-family:Georgia,serif}
.person{position:absolute;top:3068px;display:flex;align-items:center;gap:16px}
.person .avatar{width:58px;height:58px;border-radius:50%;background:linear-gradient(135deg,#d9c3a5,#8b6a4f)}
.person strong{display:block;font-size:13px;color:#222}
.person span{font-size:14px;color:#666}
.reviews{top:3178px;left:125px;width:951px;height:134px;border:1px solid #cfd3da;background:#fff;border-radius:4px}

/* cta */
.cta{top:3428px;left:0;width:1200px;height:520px;background:linear-gradient(180deg,#2b95d6,#1f7fc4 60%,#1d74b7)}
.cta h2{position:absolute;top:92px;left:0;width:1200px;text-align:center;color:#fff;font-size:44px}
.cta .call{position:absolute;top:150px;left:0;width:1200px;text-align:center;color:#fff;font-weight:700;font-size:17px}
.cta .call b{font-size:25px;margin-left:6px}
.cta-btn{position:absolute;top:218px;height:60px;border-radius:32px;border:3px solid #fff;display:flex;align-items:center;justify-content:center;gap:24px;color:#fff;text-align:center}
.cta-btn small{display:block;font-size:13px;font-weight:500}
.cta-btn b{display:block;font-size:22px}
.cta-btn .arrow{width:26px;height:26px;border-radius:50%;background:#fff;display:flex;align-items:center;justify-content:center}
.cta-btn .arrow::after{content:"";border-left:8px solid var(--navy);border-top:6px solid transparent;border-bottom:6px solid transparent;margin-left:3px}

/* footer */
.footer{top:3894px;left:0;width:1200px;height:392px;background:var(--navy-dark);color:#fff}
.footer h4{font-size:13px;font-weight:700;margin-bottom:28px;position:relative}
.footer h4::after{content:"";position:absolute;left:0;top:22px;width:26px;height:2px;background:#fff}
.footer ul{list-style:none;font-size:13px}
.footer li{margin-bottom:16px}
.footer li::before{content:"»";margin-right:14px}
.fcol{position:absolute;top:66px}
.contact-row{display:flex;gap:16px;align-items:center;font-size:12px;line-height:17px;margin-bottom:20px}
.contact-row i{width:36px;height:36px;border-radius:50%;border:1.5px solid #fff;display:flex;align-items:center;justify-content:center}
.vline{position:absolute;top:60px;width:1px;height:200px;background:rgba(255,255,255,.35)}
</style>
</head>
<body>

<!-- header -->
<header class="abs topbar">
  <div class="abs hotline">
    <svg width="44" height="40" viewBox="0 0 44 40"><path d="M6 20a16 16 0 0 1 32 0" fill="none" stroke="#1f86cf" stroke-width="3"/><rect x="2" y="18" width="8" height="12" rx="3" fill="#1f86cf"/><rect x="34" y="18" width="8" height="12" rx="3" fill="#1f86cf"/><text x="22" y="30" font-size="13" font-weight="700" fill="#1b2a6b" text-anchor="middle" font-family="Roboto,sans-serif">24</text></svg>
    <div><small>24 HOURS SERVICE</small><b>+1 555 010 0199</b></div>
  </div>
  <div class="abs socials" style="top:34px;left:562px"><i></i><i></i><i></i><i></i></div>
  <div class="abs mascot" role="img" aria-label="Green cleaner mascot holding a broom"></div>
</header>
<div class="abs brand"><span>Brightwell<br>Facility<br>Services</span></div>
<nav class="abs navbar">
  <ul class="nav"><li>HOME</li><li>ABOUT</li><li>OUR SERVICES</li><li>BLOG</li><li>REVIEWS</li><li>WHY US</li><li>CONTACT</li></ul>
</nav>

<!-- hero -->
<section class="abs hero">
  <div class="abs" style="left:0;top:0;width:1200px;height:650px;background:linear-gradient(180deg,rgba(255,255,255,.0),rgba(190,196,204,.35))" role="img" aria-label="Faded city skyline backdrop"></div>
  <h1 class="display">We Are a <em>Professional</em><br>Cleaning Service<br>Company</h1>
  <p>Lorem ipsum dolor sit amet, consectetur adipiscing elit, sed do eiusmod tempor incididunt ut labore et dolore</p>
  <div class="btn" style="left:110px;top:354px;width:198px;height:42px;background:var(--blue)">LET'S GET STARTED <span class="arrow"></span></div>
  <div class="btn" style="left:325px;top:354px;width:146px;height:42px;background:var(--navy)">BOOK NOW <span class="arrow"></span></div>
  <div class="abs slide-arrow" style="left:34px;top:240px;transform:rotate(45deg)"></div>
  <div class="abs slide-arrow" style="left:1127px;top:240px;transform:rotate(-135deg)"></div>
  <div class="abs hero-photo" role="img" aria-label="Worker in protective suit mopping a factory floor"></div>
  <svg class="abs" style="left:0;top:500px" width="1200" height="150" viewBox="0 0 1200 150" preserveAspectRatio="none">
    <path d="M0 150 L0 120 C220 40 420 60 620 90 C820 120 1000 80 1200 40 L1200 150 Z" fill="#eef0f4"/>
    <path d="M0 122 C220 42 420 62 620 92 C820 122 1000 82 1200 42 L1200 62 C1000 108 820 142 620 112 C420 82 220 70 0 142 Z" fill="#1b2a6b"/>
    <path d="M0 112 C200 50 400 55 600 78" fill="none" stroke="#1f86cf" stroke-width="4"/>
  </svg>
</section>

<!-- target -->
<section class="abs target">
  <h2 class="display section-title" style="top:78px">Our Target</h2>
  <div class="card photo-a" style="left:111px" role="img" aria-label="Glass office tower at dusk"><div class="label">COMMERCIAL BUILDINGS</div></div>
  <div class="card feature" style="left:446px">
    <div class="badge"><svg width="34" height="30" viewBox="0 0 34 30"><path d="M17 2 L30 12 H4 Z" fill="#1f86cf"/><rect x="6" y="12" width="22" height="16" fill="#1f86cf"/><rect x="14" y="18" width="6" height="10" fill="#fff"/><rect x="8" y="15" width="4" height="4" fill="#fff"/><rect x="22" y="15" width="4" height="4" fill="#fff"/></svg></div>
    <h3>SCHOOLS</h3>
    <p>Lorem ipsum dolor sit amet, consec tetur adipiscing elit, sed do eiusmotempor incididunt ut labore et dolor</p>
    <div class="go"></div>
  </div>
  <div class="card photo-b" style="left:779px" role="img" aria-label="Large hospital building"><div class="label">MEDICAL BUILDINGS</div></div>
</section>

<!-- about -->
<section class="about">
  <div class="abs about-photo" role="img" aria-label="Cleaner mopping a building entrance"></div>
  <div class="abs sparkle" style="left:126px;top:1708px;font-size:22px">+</div>
  <div class="abs sparkle" style="left:142px;top:1738px;font-size:28px">+</div>
  <div class="abs sparkle" style="left:168px;top:1768px;font-size:34px">+</div>
  <div class="abs sparkle" style="left:198px;top:1794px;font-size:44px">+</div>
  <h2 class="display">About Us</h2>
  <p>Sed ut perspiciatis unde omnis iste natus error sit voluptatem accusantium doloremque laudantium, totam rem aperiam, eaque ipsa quae ab illo inventore veritatis et quasi architecto beatae vitae dicta sunt explicabo. Nemo enim ipsam voluptatem quia voluptas sit aspernatur aut odit aut fugit, sed quia consequuntur magni dolores eos qui ratione voluptatem sequi nesciunt. Neque porro quisquam est, qui dolorem ipsum quia dolor sit amet, consectetur, adipisci velit, sed quia non numquam eius modi tempora incidunt ut labore et dolore magnam aliquam quaerat voluptatem.</p>
  <div class="btn" style="left:622px;top:1768px;width:148px;height:42px;background:var(--navy)">LEARN MORE <span class="arrow"></span></div>
</section>

<!-- why choose us -->
<section class="abs why">
  <svg class="abs" style="left:0;top:0" width="1200" height="800" viewBox="0 0 1200 800" preserveAspectRatio="none">
    <defs><linearGradient id="waterGrad" x1="0" y1="0" x2="0" y2="1"><stop offset="0" stop-color="#ffffff"/><stop offset="1" stop-color="#cfe6f5"/></linearGradient></defs>
    <path d="M0 0 H1200 V70 H0 Z" fill="url(#waterGrad)"/>
    <path d="M0 40 C300 20 500 90 800 100 C1000 108 1100 90 1200 80 L1200 770 C1000 700 800 720 600 760 C400 790 200 730 0 700 Z" fill="#2d9bd9"/>
    <path d="M0 40 C300 20 500 90 800 100 C1000 108 1100 90 1200 80 L1200 96 C1000 112 800 118 600 112 C400 104 200 70 0 60 Z" fill="#1b2a6b"/>
  </svg>
  <div class="abs" style="left:0;top:10px;width:1200px;height:80px;background:linear-gradient(180deg,rgba(255,255,255,0),rgba(160,205,235,.45))" role="img" aria-label="Clear water splash"></div>
  <h2 class="display why-head" style="top:232px;font-size:26px">Why Choose Us</h2>
  <div class="why-head" style="top:272px;font-size:18px;letter-spacing:4px">— + —</div>
  <div class="why-head" style="top:305px;font-size:16px;font-weight:700">We always believe in good service</div>

  <svg class="abs" style="left:340px;top:400px" width="520" height="300" viewBox="0 0 520 300">
    <path d="M20 290 A240 240 0 0 1 500 290" fill="#fff" stroke="#1b2a6b" stroke-width="14"/>
    <path d="M60 290 A200 200 0 0 1 460 290" fill="#f4f7fb"/>
  </svg>
  <div class="abs" style="left:420px;top:514px;width:360px;text-align:center;font-family:'Roboto',sans-serif;font-weight:700;font-size:34px;color:#1b2a6b;letter-spacing:3px">BRIGHTWELL</div>
  <div class="abs" style="left:520px;top:565px;width:160px;height:140px;border-radius:70px 70px 0 0;background:var(--green)" role="img" aria-label="Mascot cleaner holding a broom"></div>

  <div class="why-item left" style="right:754px;top:402px">We Always take care<br>of you</div>
  <div class="why-item left" style="right:857px;top:496px">We provide same day<br>Service</div>
  <div class="why-item left" style="right:897px;top:626px">No Surprise and no hidden<br>Charges</div>
  <div class="why-item" style="left:744px;top:395px">Guaranteed Work with 100%<br>satisfaction</div>
  <div class="why-item" style="left:867px;top:496px">We are available all<br>time</div>
  <div class="why-item" style="left:909px;top:638px">We provide best services<br>to customers</div>

  <div class="why-icon" style="left:466px;top:403px"><svg width="34" height="30" viewBox="0 0 34 30"><path d="M17 14 C10 8 8 2 13 2 C15 2 17 4 17 6 C17 4 19 2 21 2 C26 2 24 8 17 14Z" fill="#3bb54a"/><path d="M2 22 H12 L20 26 L32 20" fill="none" stroke="#3bb54a" stroke-width="3"/></svg></div>
  <div class="why-icon" style="left:365px;top:496px"><svg width="30" height="30" viewBox="0 0 30 30"><circle cx="15" cy="8" r="5" fill="#3bb54a"/><path d="M5 28 V20 H25 V28Z" fill="#3bb54a"/></svg></div>
  <div class="why-icon" style="left:325px;top:625px;font-weight:700;font-size:11px;color:#3bb54a;line-height:11px;text-align:center">NO<br>FEES</div>
  <div class="why-icon" style="left:646px;top:397px"><svg width="30" height="30" viewBox="0 0 30 30"><circle cx="15" cy="13" r="10" fill="#3bb54a"/><path d="M10 13 l4 4 l7 -7" fill="none" stroke="#fff" stroke-width="2.5"/><path d="M9 22 l-3 7 l5 -2 M21 22 l3 7 l-5 -2" fill="#3bb54a" stroke="#3bb54a" stroke-width="2"/></svg></div>
  <div class="why-icon" style="left:777px;top:500px;font-weight:700;color:#3bb54a;font-size:18px">24</div>
  <div class="why-icon" style="left:821px;top:625px"><svg width="30" height="30" viewBox="0 0 30 30"><circle cx="15" cy="15" r="11" fill="none" stroke="#3bb54a" stroke-width="4" stroke-dasharray="4 2"/><circle cx="15" cy="15" r="5" fill="#3bb54a"/></svg></div>
</section>

<!-- testimonials -->
<h2 class="display section-title" style="top:2806px;font-size:26px">What Our Clients Say</h2>
<div class="abs" style="top:2846px;left:0;width:1200px;text-align:center;color:var(--blue);letter-spacing:4px">— + —</div>

<div class="quote" style="left:111px">Sed ut perspiciatis unde omnis istenatus error sit voluptatem accusandoloremque laudantium, totam aperiam<b>“</b></div>
<div class="quote" style="left:446px">Sed ut perspiciatis unde omnis istenatus error sit voluptatem accusandoloremque laudantium, totam aperiam<b>“</b></div>
<div class="quote" style="left:783px">Sed ut perspiciatis unde omnis istenatus error sit voluptatem accusandoloremque laudantium, totam aperiam<b>“</b></div>

<div class="person" style="left:120px"><div class="avatar" role="img" aria-label="Client portrait"></div><div><strong>SAM RIVERA</strong><span>Businessman</span></div></div>
<div class="person" style="left:457px"><div class="avatar" role="img" aria-label="Client portrait"></div><div><strong>SAM RIVERA</strong><span>Businessman</span></div></div>
<div class="person" style="left:794px"><div class="avatar" role="img" aria-label="Client portrait"></div><div><strong>SAM RIVERA</strong><span>Businessman</span></div></div>

<div class="abs reviews">
  <div class="abs" style="left:30px;top:52px;font-size:20px;color:#4a5160">Verified reviews</div>
  <div class="abs" style="left:162px;top:45px;font-size:13px;color:#f2b01e;letter-spacing:2px">★★★★★</div>
  <div class="abs" style="left:162px;top:68px;font-size:14px;color:#555"><b style="color:#111">500+</b> 5 Star Reviews</div>
  <div class="btn" style="left:360px;top:36px;width:268px;height:62px;background:var(--blue);border:3px solid var(--navy);border-radius:32px;font-size:14px;text-align:center;line-height:17px">CHECK OUT OUR<br>CUSTOMER REVIEWS <span class="arrow" style="width:22px;height:22px"></span></div>
  <div class="abs" style="left:684px;top:44px;width:112px;height:44px;border-radius:4px;background:var(--navy)"></div>
  <div class="abs" style="left:845px;top:40px;font-size:14px;color:var(--navy);letter-spacing:2px">★★★★★</div>
  <div class="abs" style="left:845px;top:62px;font-size:15px;color:#555"><b style="color:#111">A+</b> Rating</div>
</div>

<!-- cta -->
<section class="abs cta">
  <div class="abs" style="left:0;top:0;width:1200px;height:520px;background:linear-gradient(90deg,rgba(255,255,255,.08),rgba(20,70,130,.15),rgba(255,255,255,.06))" role="img" aria-label="Cleaning staff at work in an office"></div>
  <h2 class="display">24 Hour same day service</h2>
  <div class="call">Call Us Today ! <b>+ 1 555 010 0199</b></div>
  <div class="cta-btn" style="left:283px;width:264px;background:var(--navy)"><div><small>CLICK HERE TO</small><b>BOOK ONLINE</b></div><span class="arrow"></span></div>
  <div class="abs" style="left:583px;top:236px;color:#fff;font-weight:700;font-size:21px">OR</div>
  <div class="cta-btn" style="left:652px;width:264px;background:var(--green)"><div><small>CLICK TO GET UNLIMITED</small><b>FREE CALL</b></div><span class="arrow"></span></div>
  <svg class="abs" style="left:0;top:370px" width="1200" height="150" viewBox="0 0 1200 150" preserveAspectRatio="none">
    <path d="M0 110 C250 140 450 70 650 70 C850 70 1000 40 1200 0 L1200 150 L0 150 Z" fill="#131e4f"/>
    <path d="M0 96 C250 126 450 58 650 58 C850 58 1000 28 1200 -10" fill="none" stroke="#fff" stroke-width="6"/>
  </svg>
</section>

<!-- footer -->
<footer class="abs footer">
  <div class="abs" style="left:146px;top:70px;width:140px;height:140px;border-radius:50%;border:3px solid #fff;display:flex;align-items:center;justify-content:center;text-align:center;font-weight:700;font-size:15px;line-height:1.2">Brightwell<br>Facility<br>Services</div>
  <div class="abs socials" style="left:144px;top:224px"><i></i><i></i><i></i><i></i></div>
  <div class="vline" style="left:336px"></div>
  <div class="vline" style="left:557px"></div>
  <div class="vline" style="left:832px"></div>
  <div class="fcol" style="left:391px"><h4>QUICK LINKS</h4><ul><li>Home</li><li>About Us</li><li>Our Services</li><li>Why Us</li><li>Contact Us</li></ul></div>
  <div class="fcol" style="left:602px"><h4>CONTACT US</h4>
    <div class="contact-row"><i><svg width="14" height="18" viewBox="0 0 14 18"><path d="M7 1a6 6 0 0 1 6 6c0 4-6 10-6 10S1 11 1 7a6 6 0 0 1 6-6z" fill="none" stroke="#fff" stroke-width="1.6"/><circle cx="7" cy="7" r="2" fill="#fff"/></svg></i><span>PO Box 410 Fairview 90210<br>United States</span></div>
    <div class="contact-row"><i><svg width="16" height="16" viewBox="0 0 16 16"><path d="M3 1 L6 4 L4.5 6 C5.5 8 8 10.5 10 11.5 L12 10 L15 13 L13 15 C7 15 1 9 1 3 Z" fill="#fff"/></svg></i><span>+1 555 010 0199<br>+1 555 010 0177</span></div>
    <div class="contact-row"><i><svg width="16" height="12" viewBox="0 0 16 12"><rect x="0.5" y="0.5" width="15" height="11" fill="#fff"/><path d="M1 1 L8 7 L15 1" fill="none" stroke="#131e4f" stroke-width="1.5"/></svg></i><span>info@brightwellfs.com</span></div>
  </div>
  <div class="fcol" style="left:877px"><h4>OTHER LINKS</h4><ul><li>Company Information</li><li>Our Partners</li><li>Terms &amp; Conditions</li><li>Privacy Plocy</li><li>FAQ</li></ul></div>
  <div class="abs" style="left:104px;top:311px;width:992px;height:1px;background:rgba(255,255,255,.35)"></div>
  <div class="abs" style="left:0;top:340px;width:1200px;text-align:center;font-size:13px">© 2022 Brightwell Facility Services. All Rights Reserved</div>
</footer>

</body>
</html>
```